Craft Portuguese Gin Distillery launching new gin into international market

We are going to launch two new gins:
1. An aged version of the Velmar Caspo, one that already exists - aged in port casks. This will be a 500ml bottle. Bottle not defined yet - Check www.sipvorlane.com
2. A new gin with a lower ABV (lower strength), to satisfy both connoisseurs and "ordinary"; customers. We want to stay with the branding line. The label must appeal to the customer to try the gin, must stand out on a shelf that is full of other spirits. We want to pass on the idea of a premium gin. No botle selected yet. For this gin we may use only a label or a complete decorated bottle. Take care of the legal demands that have to go onto the label - we can help with this later on.
Notes:
- The distillery's name is Orvane - Premium Spirits (logo attached)
- Our first gin is called Velmar Caspo (logo attached)
- No names selected for either of these gins;
- We have a moto that we would like to see on the bottle:
"Drink to remember, not to forget!";
- Our gins have a unique botanical that is fig tree bark, we are portuguese and we are very fond of the fig image attached.
- Attached we send some documents where you can learn about the story of the gin and also for you to get to know us little better.
- If you wish to suggest a bottle, please look-up these two web sites:
https://www.brolukvessel.com/en
https://www.quandimflask.com/
Please contact us for any further information.
Thank you

Target Market(s)

Spirits worldwide

Colors

Designer to choose colors to be used in the design.

Requirements
Must have
• Mandatory Legal information for spirit drinks
• Place for:
• - Producer / bottler (name and addres)
• - Origin fo the product - Product from Portugal
• - ABV and Capacity
• - Type of product: "Londo Dry Gin"
Nice to have
• - We have a moto that we would like to see on the bottle:
• "quot;Drink to remember, not to forget!";
• - Our gins have a unique botanical that is fig tree bark, we are portuguese and we are very fond of the fig image attached.

```html
<!DOCTYPE html>
<html lang="en">
<head>
<meta charset="utf-8">
<title>Velmar Caspo – London Dry Gin Label</title>
<link rel="stylesheet" href="https://fonts.googleapis.com/css2?family=Playfair+Display:wght@700&family=Great+Vibes&family=Roboto+Condensed:wght@400;700&display=swap">
<style>
  :root {
    --backdrop: #e9e4dc;
    --label-paper: #fbfaf6;
    --fig-tone: #e4d9c2;
    --fig-tone-light: #f2ece0;
    --panel-black: #161515;
    --accent-red: #a3161b;
    --ink-light: #f4f1ea;
    --ink-dark: #2a2826;
  }
  * { margin: 0; padding: 0; box-sizing: border-box; }
  html, body {
    width: 971px; height: 1200px; overflow: hidden;
    background: var(--backdrop);
  }
  .canvas { position: relative; width: 971px; height: 1200px; }
  .label {
    position: absolute; left: 85px; top: 85px;
    width: 800px; height: 1030px;
    background: var(--label-paper);
    box-shadow: 0 6px 24px rgba(0,0,0,.12);
    overflow: hidden;
  }
  .fig-artwork {
    position: absolute; left: 150px; top: 30px;
    width: 620px; height: 970px;
    border-radius: 48% 52% 46% 54% / 40% 38% 62% 60%;
    background: linear-gradient(160deg, var(--fig-tone) 0%, var(--fig-tone-light) 55%, var(--fig-tone) 100%);
  }
  .type-strip {
    position: absolute; left: 0; top: 90px; width: 44px; height: 300px;
    background: var(--accent-red);
    display: flex; align-items: center; justify-content: center;
  }
  .type-strip span {
    transform: rotate(-90deg); white-space: nowrap;
    font-family: "Roboto Condensed", sans-serif; font-weight: 700;
    font-size: 15px; letter-spacing: 3px; color: var(--ink-light);
  }
  .brand-panel {
    position: absolute; left: 44px; top: 200px; width: 430px; height: 380px;
    background: var(--panel-black);
    color: var(--ink-light);
    padding: 70px 34px 0 40px;
  }
  .brand-name {
    font-family: "Playfair Display", serif; font-weight: 700;
    font-size: 50px; line-height: 1; text-align: center;
  }
  .motto {
    font-family: "Great Vibes", cursive; font-size: 29px;
    margin-top: 40px; white-space: nowrap;
  }
  .details {
    margin-top: 18px;
    font-family: "Roboto Condensed", sans-serif; font-size: 16px;
    letter-spacing: 2.5px; line-height: 1.7;
  }
  .details .rule {
    display: block; height: 1px; background: var(--ink-light);
    opacity: .6; margin: 6px 0;
  }
  .legal {
    position: absolute; left: 70px; top: 830px;
    font-family: "Roboto Condensed", sans-serif; font-weight: 700;
    font-size: 16px; letter-spacing: 2px; color: var(--ink-dark);
  }
</style>
</head>
<body>
<main class="canvas">
  <section class="label">
    <div class="fig-artwork" role="img" aria-label="Engraved fig branch with leaves and fruit in pale beige"></div>
    <div class="type-strip"><span>LONDON DRY GIN</span></div>
    <div class="brand-panel">
      <h1 class="brand-name">Velmar Caspo</h1>
      <p class="motto">Drink to Remember, Not to Forget</p>
      <p class="details">
        <span class="rule"></span>
        BOTTLER NAME · LISBON 2019
        <span class="rule"></span>
        PRODUCT FROM PORTUGAL
      </p>
    </div>
    <p class="legal">58% ABV · 70 CL</p>
  </section>
</main>
</body>
</html>
```